Home Security Website

This website is for a home security website. We feature the best in home security products and monitoring. The website name is Hearthwise Crew.
We would like a direct response design with a large hero image.
The final design should incorporate safety, security, and family. Please do not use scare tactics in the design.
Target Market(s)
Women, primarily
Industry/Entity Type
Security
Requirements
Must have
- Must have a clear Call to Action Area for telephone and lead gen form
Nice to have
- - Large heroes with lifestyle images of family - security
- below the fold text area with boxes
Should not have
- no scare tactics please
DO NOT submit designs with DARK or BLACK backgrounds

```html
<!DOCTYPE html>
<html lang="en">
<head>
<meta charset="utf-8">
<title>Hearthwise Crew – Home Security</title>
<link href="https://fonts.googleapis.com/css2?family=Open+Sans:wght@300;400;600;700&family=Rokkitt:wght@400;500&display=swap" rel="stylesheet">
<style>
:root{
  --cream:#fdf0d8;
  --cream-deep:#f9e2b3;
  --ink:#333333;
  --navy:#1d2454;
  --navy-light:#3c4585;
  --link:#1a5ab0;
  --title:#2463b3;
  --quote-blue:#2160b8;
  --quote-dark:#164a94;
  --green:#8cc821;
  --green-dark:#5f9a0e;
  --orange:#ff6a10;
  --orange-dark:#c23800;
  --gold:#ffc93a;
  --footer-grey:#ebebea;
  --muted:#555555;
}
*{margin:0;padding:0;box-sizing:border-box}
html,body{width:942px;height:1200px;overflow:hidden}
body{background:linear-gradient(90deg,var(--cream) 0%,var(--cream) 55%,var(--cream-deep) 100%);font-family:"Open Sans",sans-serif;color:var(--ink)}
.page{position:relative;width:1020px;height:1300px;transform:scale(0.923529);transform-origin:0 0}
.abs{position:absolute}

.topbar{left:0;top:0;width:1020px;height:27px;background:linear-gradient(#fff,#f1f1f1);border-bottom:1px solid #e2dccf;font-size:11px}
.topbar a{position:absolute;top:6px;color:#222;text-decoration:none}
.topbar .sep{position:absolute;top:5px;color:#222}
.user-icon{position:absolute;left:857px;top:5px}

.brand{left:31px;top:32px;font-family:"Open Sans",sans-serif;font-weight:600;font-size:31px;line-height:38px;color:var(--navy)}

.call-cta{left:700px;top:36px;width:290px;height:32px;display:flex;align-items:center;justify-content:flex-end;gap:8px;color:var(--navy);font-size:13px}
.call-cta strong{font-size:19px;font-weight:700;color:var(--title)}

.mainnav{left:30px;top:73px;width:960px;height:40px;border-radius:4px;background:linear-gradient(var(--navy-light),var(--navy) 55%,#252c63);display:flex;border:1px solid #141a44}
.mainnav a{display:flex;align-items:center;justify-content:center;color:#fff;font-weight:700;font-size:12.5px;text-decoration:none;border-right:1px solid #5b63a0}
.mainnav a:last-child{border-right:none}

.hero-photo{left:30px;top:118px;width:960px;height:390px;background:radial-gradient(ellipse at 50% 40%,#e6c6a6 0%,#d8b08e 30%,#b7a394 55%,rgba(253,240,216,0) 80%),linear-gradient(180deg,rgba(253,240,216,.3),#cdb8a0)}

.promo-arrow{left:105px;top:474px}
.promo-kicker{left:258px;top:501px;font-size:12.5px;font-weight:700;color:#2d4a06}
.promo-head{left:256px;top:513px;font-size:37px;color:#fff;line-height:1;text-shadow:0 1px 2px rgba(0,0,0,.3)}
.promo-head b{font-weight:700}
.promo-head span{font-weight:300}
.promo-sub{left:259px;top:550px;font-size:14px;color:#fff}

.apply-btn{left:30px;top:498px;width:220px;height:70px;border-radius:6px;background:linear-gradient(var(--orange),var(--orange-dark));box-shadow:0 3px 5px rgba(0,0,0,.3);color:#fff;font-size:30px;display:flex;align-items:center;justify-content:center;text-shadow:0 1px 2px rgba(0,0,0,.4)}

.quote{left:630px;top:401px;width:360px;height:240px;border-radius:5px;background:repeating-linear-gradient(90deg,var(--quote-blue) 0 2px,#1d59ad 2px 4px);border:1px solid var(--quote-dark)}
.quote h2{position:absolute;left:23px;top:14px;font-size:26px;font-weight:600;color:#fff;letter-spacing:.5px}
.quote .rule{position:absolute;left:0;top:56px;width:100%;height:1px;background:#4a80cc}
.quote label{position:absolute;font-size:11px;color:#fff}
.quote .field{position:absolute;height:25px;background:#fff;border:1px solid #0e3b7a;border-radius:2px}
.quote .get{position:absolute;left:245px;top:186px;width:79px;height:22px;border-radius:6px;background:linear-gradient(#ffe27a,var(--gold) 50%,#f0a800);border:1px solid #c98a00;font-size:11px;font-weight:700;color:#1d2454;display:flex;align-items:center;justify-content:center;letter-spacing:.5px}

.title{font-family:"Rokkitt",serif;font-size:29px;color:var(--title);font-weight:400}
.body-text{font-size:12.8px;line-height:18px;color:var(--ink)}
.more{font-size:12.5px;font-weight:700;color:var(--link);text-decoration:none}

.eyebrow{left:631px;top:671px;font-size:12.5px;color:#333}
.avatar{left:633px;top:739px;width:75px;height:93px;background:linear-gradient(#dfe6ea,#c7b79d 55%,#9fb4bc)}

.divider{left:0;top:890px;width:1020px;height:1px;background:#f3e2c4;box-shadow:0 1px 0 #fff8ea}

.feature h3{font-size:11.5px;font-weight:700;color:#222;margin-bottom:9px}
.feature ul{list-style:none}
.feature li{font-size:11.3px;color:var(--link);line-height:19px;padding-left:10px;position:relative}
.feature li::before{content:"";position:absolute;left:0;top:8px;width:3px;height:3px;border-radius:50%;background:var(--link)}
.feature .more{position:absolute;top:104px;left:0}

.footer-box{left:30px;top:1080px;width:960px;height:168px;background:linear-gradient(#f9f9f8,var(--footer-grey))}
.fcol{position:absolute;top:23px;width:185px}
.fcol h4{font-size:12.5px;font-weight:600;color:#444;padding-bottom:14px;border-bottom:1px solid #cfcfcf}
.fcol a{display:block;font-size:11.3px;color:#555;text-decoration:none;height:25px;line-height:26px;border-bottom:1px dotted #bdbdbd}
.fcol a:last-child{border-bottom:none}
.fcol p{font-size:11.3px;line-height:16px;color:#555;padding-top:8px}

.legal{left:31px;top:1267px;font-size:11.3px;color:#555}
.legal span{margin:0 5px;color:#777}
</style>
</head>
<body>
<div class="page">

  <header>
    <div class="abs topbar">
      <a style="left:486px">Home</a><span class="sep" style="left:531px">|</span>
      <a style="left:550px">Help</a><span class="sep" style="left:589px">|</span>
      <a style="left:607px">My Account</a><span class="sep" style="left:683px">|</span>
      <a style="left:701px">Store Finder</a>
      <svg class="user-icon" width="14" height="15" viewBox="0 0 14 15" aria-hidden="true"><circle cx="7" cy="4" r="3.6" fill="#222"/><path d="M0 15c0-5 3-7 7-7s7 2 7 7z" fill="#222"/></svg>
      <a style="left:886px">Login</a><span class="sep" style="left:931px">|</span>
      <a style="left:949px">Register</a>
    </div>

    <div class="abs brand">Hearthwise Crew</div>

    <div class="abs call-cta">
      <svg width="18" height="18" viewBox="0 0 24 24" aria-hidden="true"><path fill="#1d2454" d="M6.6 10.8a15.1 15.1 0 0 0 6.6 6.6l2.2-2.2c.3-.3.7-.4 1-.2 1.1.4 2.3.6 3.6.6.6 0 1 .4 1 1V20c0 .6-.4 1-1 1A17 17 0 0 1 3 4c0-.6.4-1 1-1h3.5c.6 0 1 .4 1 1 0 1.3.2 2.5.6 3.6.1.3 0 .7-.2 1z"/></svg>
      <span>Call for a free quote</span><strong>(555) 014-2290</strong>
    </div>

    <nav class="abs mainnav">
      <a style="width:158px">Alarm Systems</a>
      <a style="width:114px">Door Bells</a>
      <a style="width:110px">Intercoms</a>
      <a style="width:215px">Video Surveillance Systems</a>
      <a style="width:138px">Security Lights</a>
      <a style="width:106px">Packages</a>
      <a style="width:117px">Contact</a>
    </nav>
  </header>

  <section class="hero">
    <div class="abs hero-photo" role="img" aria-label="Lifestyle photo of a smiling multi-generation family looking upward together"></div>

    <svg class="abs promo-arrow" width="482" height="122" viewBox="0 0 482 122" aria-hidden="true">
      <defs><linearGradient id="arrowFill" x1="0" y1="0" x2="0" y2="1"><stop offset="0" stop-color="#a6dc2c"/><stop offset="1" stop-color="#6fae12"/></linearGradient></defs>
      <polygon points="0,2 420,2 480,61 420,119 0,119" fill="url(#arrowFill)"/>
    </svg>
    <div class="abs promo-kicker">AETERNO CONVENIRE DETRAXIT</div>
    <div class="abs promo-head"><b>ROCK</b> <span>solid locks</span></div>
    <div class="abs promo-sub">Assum numquam cum id</div>

    <div class="abs apply-btn">Apply Now</div>

    <form class="abs quote">
      <h2>FREE QUOTE</h2>
      <div class="rule"></div>
      <label style="left:25px;top:70px">Name</label>
      <div class="field" style="left:24px;top:86px;width:132px"></div>
      <label style="left:176px;top:70px">Phone</label>
      <div class="field" style="left:175px;top:86px;width:132px"></div>
      <label style="left:25px;top:119px">City</label>
      <div class="field" style="left:24px;top:135px;width:132px"></div>
      <label style="left:176px;top:119px">Zip</label>
      <div class="field" style="left:175px;top:135px;width:79px"></div>
      <label style="left:25px;top:168px">Email</label>
      <div class="field" style="left:24px;top:184px;width:203px"></div>
      <div class="get">GET QUOTE</div>
    </form>
  </section>

  <section class="intro">
    <h1 class="abs title" style="left:30px;top:614px">Title One Goes Here</h1>
    <p class="abs body-text" style="left:30px;top:667px;width:560px">Sale omittam mei ne. Id error nonumy est, ius an ferri nulla persecuti, in quod solum fabellas est. Est ad mollis utamur fuisset, animal voluptatum nec at, putant iisque nec ex. Id vidisse alterum sit. Ex duo apeirian molestiae contentiones.</p>
    <p class="abs body-text" style="left:30px;top:736px;width:560px">Assum numquam cum id, id aliquid invidunt his. Populo eirmod urbanitas usu ex. Duo viderer voluptaria cu, et has persius aliquid omnesque, ius te feugait vivendo laboramus. Sumo quidam quo in, his ut graeci discere blandit. Has in tota ullamcorper, quaeque sapientem principes ex mel, paulo mucius duo an. Eam in semper periculis, pri ponderum lobortis maluisset te, electram erroribus splendide ea vim. Novum putant corpora mel in, nostrud molestie ad vix.</p>
    <a class="abs more" style="left:30px;top:857px">Read more</a>
  </section>

  <section class="testimonial">
    <div class="abs eyebrow">TESTIMONIALS</div>
    <h2 class="abs title" style="left:631px;top:685px">Title Two Goes Here</h2>
    <div class="abs avatar" role="img" aria-label="Portrait photo of a smiling customer"></div>
    <p class="abs body-text" style="left:732px;top:736px;width:255px">Atqui viderer mei at, no doctus copiosae sea. His an debet malorum, pro te sumo latine signiferumque. Quas consectetuer ius eu, eu paulo scripta scriptorem sit, est erant clita periculis ad. Quis facilisis pri an, equidem lucilius persecuti et vis. Ius</p>
    <a class="abs more" style="left:732px;top:857px">Read more</a>
  </section>

  <div class="abs divider"></div>

  <section class="features">
    <div class="abs feature" style="left:30px;top:921px;width:310px">
      <h3>Sint eleifend id nam, in qui epicuri accusamus</h3>
      <ul><li>Quod erat dolorum his ne, sed debet iisque eu, cu vix</li><li>At verear epicuri mei, partem labitur virtute pro no</li><li>No vim adhuc aperiam virtute, et quo essent dicunt</li></ul>
      <a class="more">More »</a>
    </div>
    <div class="abs feature" style="left:361px;top:921px;width:310px">
      <h3>Sint eleifend id nam, in qui epicuri accusamus</h3>
      <ul><li>Quod erat dolorum his ne, sed debet iisque eu, cu vix</li><li>At verear epicuri mei, partem labitur virtute pro no</li><li>No vim adhuc aperiam virtute, et quo essent dicunt</li></ul>
      <a class="more">More »</a>
    </div>
    <div class="abs feature" style="left:692px;top:921px;width:310px">
      <h3>Sint eleifend id nam, in qui epicuri accusamus</h3>
      <ul><li>Quod erat dolorum his ne, sed debet iisque eu, cu vix</li><li>At verear epicuri mei, partem labitur virtute pro no</li><li>No vim adhuc aperiam virtute, et quo essent dicunt</li></ul>
      <a class="more">More »</a>
    </div>
  </section>

  <footer>
    <div class="abs footer-box">
      <div class="fcol" style="left:16px">
        <h4>Modus Graece Detracto</h4>
        <a>Reformidans luvaret</a><a>Consequuntur</a><a>Ullamcorper Essent</a><a>Gloriatur Dicam</a>
      </div>
      <div class="fcol" style="left:224px">
        <h4>Modus Graece Detracto</h4>
        <a>Reformidans luvaret</a><a>Consequuntur</a><a>Ullamcorper Essent</a><a>Gloriatur Dicam</a>
      </div>
      <div class="fcol" style="left:432px">
        <h4>Modus Graece Detracto</h4>
        <a>Reformidans luvaret</a><a>Consequuntur</a><a>Ullamcorper Essent</a><a>Gloriatur Dicam</a>
      </div>
      <div class="fcol" style="left:659px;width:280px">
        <h4 style="width:185px">Nulla Dolore Aliquando</h4>
        <p>Usu ea prima audiam virtute. Ex eos novum fastidii accusata, dictas interpretaris vix ut. Id fastidii sensibus maluisset usu, an vis oratio eligendi necessitatibus. Sit id fugit diceret molestiae, te perpetua repudiandae sed, has ea nulla iudico.</p>
      </div>
    </div>
    <div class="abs legal">Privacy Policy<span>|</span>Terms &amp; Conditions<span>|</span>© 2013 Hearthwise Crew. All Rights Reserved</div>
  </footer>

</div>
</body>
</html>
```